Business Card Design Project

We are a construction company in Orange County, CA. We need a two sided business card. We would like the back to be our logo with web URL. Front should included Name, title, address, phone, fax and email address.

our address is
627 West Marrow Blvd, Suite 305
Larkmont, CA 92714

Our logo files are attached.

Construction

```html
<!DOCTYPE html>
<html lang="en">
<head>
<meta charset="utf-8">
<title>Halver Business Card</title>
<link rel="stylesheet" href="https://fonts.googleapis.com/css2?family=Arimo:wght@400;700&display=swap">
<style>
  :root {
    --brand-blue: #1f4e85;
    --name-blue: #1a5fa8;
    --ink: #1a1a1a;
    --card-white: #ffffff;
    --canvas: #e9ebee;
  }
  * { box-sizing: border-box; margin: 0; padding: 0; }
  html, body {
    width: 1200px;
    height: 900px;
    overflow: hidden;
    background: var(--canvas);
    font-family: "Arimo", Arial, sans-serif;
  }
  .canvas {
    position: relative;
    width: 1200px;
    height: 900px;
  }
  .card {
    position: absolute;
    width: 560px;
    height: 320px;
    border-radius: 22px;
    box-shadow: 0 10px 28px rgba(0,0,0,0.18);
    overflow: hidden;
  }
  /* Back side */
  .card-back {
    left: 100px;
    top: 90px;
    background: var(--brand-blue);
  }
  .card-back .wordmark {
    position: absolute;
    left: 70px;
    top: 112px;
    font-size: 76px;
    font-weight: 700;
    letter-spacing: 1px;
    color: var(--card-white);
    line-height: 1;
  }
  .card-back .web {
    position: absolute;
    right: 34px;
    bottom: 28px;
    font-size: 15px;
    color: var(--card-white);
    font-family: "Times New Roman", serif;
  }
  /* Front side */
  .card-front {
    left: 540px;
    top: 490px;
    background: var(--card-white);
  }
  .card-front .edge-tab {
    position: absolute;
    right: 0;
    top: 40px;
    width: 10px;
    height: 44px;
    background: var(--brand-blue);
  }
  .card-front .wordmark {
    position: absolute;
    right: 40px;
    top: 34px;
    font-size: 48px;
    font-weight: 700;
    color: var(--brand-blue);
    line-height: 1;
  }
  .holder {
    position: absolute;
    left: 40px;
    top: 128px;
  }
  .holder .name {
    font-size: 20px;
    font-weight: 700;
    color: var(--name-blue);
  }
  .holder .title {
    font-size: 11px;
    color: var(--ink);
    margin-top: 3px;
  }
  .contact {
    position: absolute;
    right: 22px;
    top: 128px;
    text-align: right;
  }
  .address {
    font-size: 15px;
    color: var(--name-blue);
    line-height: 1.2;
    margin-right: 34px;
    margin-bottom: 10px;
  }
  .contact-line {
    display: flex;
    justify-content: flex-end;
    align-items: center;
    gap: 14px;
    font-size: 16px;
    color: var(--ink);
    height: 22px;
  }
  .contact-line svg {
    width: 18px;
    height: 18px;
    flex: none;
  }
  .icon { fill: none; stroke: var(--name-blue); stroke-width: 1.6; }
  .icon-fill { fill: var(--name-blue); }
</style>
</head>
<body>
<main class="canvas">

  <section class="card card-back" aria-label="Card back">
    <div class="wordmark">HALVER</div>
    <div class="web">www.yourdomain.com</div>
  </section>

  <section class="card card-front" aria-label="Card front">
    <div class="edge-tab"></div>
    <div class="wordmark">HALVER</div>

    <div class="holder">
      <div class="name">Marcus Delaney</div>
      <div class="title">General Manager</div>
    </div>

    <div class="contact">
      <div class="address">627 West Marrow Blvd, Suite 305<br>Larkmont, CA 92714</div>

      <div class="contact-line">
        <span>(00) 123-4567-890</span>
        <svg viewBox="0 0 18 18" aria-hidden="true">
          <path class="icon-fill" d="M2 7c0-3 14-3 14 0v1h-4V7H6v1H2z"/>
          <rect class="icon-fill" x="4" y="9" width="10" height="6" rx="1"/>
        </svg>
      </div>

      <div class="contact-line">
        <span>(00) 123-4567-890</span>
        <svg viewBox="0 0 18 18" aria-hidden="true">
          <rect class="icon" x="3" y="2" width="12" height="14" rx="1"/>
          <line class="icon" x1="6" y1="6" x2="12" y2="6"/>
          <line class="icon" x1="6" y1="9" x2="12" y2="9"/>
          <line class="icon" x1="6" y1="12" x2="12" y2="12"/>
        </svg>
      </div>

      <div class="contact-line">
        <span>info@yourdomain.com</span>
        <svg viewBox="0 0 18 18" aria-hidden="true">
          <rect class="icon" x="2" y="5" width="14" height="10" rx="1"/>
          <polyline class="icon" points="2,5 9,11 16,5"/>
        </svg>
      </div>

      <div class="contact-line">
        <span>www.yourdomain.com</span>
        <svg viewBox="0 0 18 18" aria-hidden="true">
          <circle class="icon" cx="9" cy="9" r="7"/>
          <ellipse class="icon" cx="9" cy="9" rx="3" ry="7"/>
          <line class="icon" x1="2" y1="9" x2="16" y2="9"/>
        </svg>
      </div>
    </div>
  </section>

</main>
</body>
</html>
```